Visit card

Industry/Entity Type

Health Care

Contact Information for Business Card

O VITAL SYSTEMIQUE
Odile Ferrand - chef de Projet

Requirements
Must have
• 318 Rue des Tilleuls Verts 47150 BÉTHUNE Tel: 33 (0) 487 204 615 Mobile: 06 42 93 17 58 Web: www.cliniqorvane.example Contact: o.ferrand@o-vitalsystemique.example
Should not have
• Respect for color

```html
<!DOCTYPE html>
<html lang="fr">
<head>
<meta charset="utf-8">
<title>O Vital Systemique – Carte de visite</title>
<link href="https://fonts.googleapis.com/css2?family=Open+Sans:wght@400;600;700&display=swap" rel="stylesheet">
<style>
  :root {
    --red: #e31e2a;
    --charcoal: #3d3d3f;
    --ink: #1e1e1e;
    --paper: #ffffff;
    --backdrop: #e9e9ea;
  }
  * { margin: 0; padding: 0; box-sizing: border-box; }
  html, body {
    width: 1200px; height: 900px; overflow: hidden;
    background: var(--backdrop);
    font-family: "Open Sans", Arial, sans-serif;
  }
  .canvas { position: relative; width: 1200px; height: 900px; }
  .card {
    position: absolute; left: 285px; width: 630px; height: 360px;
    background: var(--paper); overflow: hidden;
    box-shadow: 0 6px 18px rgba(0,0,0,0.12);
  }
  .card--back { top: 50px; }
  .card--front { top: 480px; }

  .brand { display: flex; align-items: center; gap: 12px; }
  .brand__dot {
    width: 34px; height: 34px; border-radius: 50%;
    background: var(--red); flex: none;
  }
  .brand__name {
    font-weight: 700; color: var(--charcoal);
    font-size: 21px; letter-spacing: 1.5px; white-space: nowrap;
  }

  .card--back .brand {
    position: absolute; left: 50%; top: 50%;
    transform: translate(-50%, -50%);
  }
  .card--back .brand__dot { width: 46px; height: 46px; }
  .card--back .brand__name { font-size: 27px; }
  .accent-lines { position: absolute; inset: 0; }

  .card--front .brand { position: absolute; left: 42px; top: 42px; }
  .divider {
    position: absolute; left: 0; right: 0; top: 238px; height: 9px;
    background: var(--charcoal);
  }
  .band {
    position: absolute; left: 0; right: 0; top: 255px; bottom: 0;
    background: var(--red);
  }
  .person {
    position: absolute; right: 40px; top: 108px; text-align: right;
    color: var(--ink);
  }
  .person__name { font-weight: 700; font-size: 17px; line-height: 1.2; }
  .person__role { font-size: 13px; color: var(--charcoal); margin-bottom: 10px; }
  .contact-list { list-style: none; font-size: 11.5px; line-height: 1.5; color: var(--ink); }
  .contact-list li { display: flex; justify-content: flex-end; align-items: center; gap: 8px; }
  .contact-list .icon { width: 11px; height: 11px; flex: none; }
  .online {
    position: absolute; right: 40px; top: 290px; list-style: none;
    color: var(--paper); font-size: 12.5px; line-height: 1.6; text-align: right;
  }
  .online li { display: flex; justify-content: flex-end; align-items: center; gap: 8px; }
  .online .icon { width: 12px; height: 12px; flex: none; }
</style>
</head>
<body>
<main class="canvas">

  <section class="card card--back" aria-label="Verso de la carte">
    <svg class="accent-lines" viewBox="0 0 630 360" aria-hidden="true">
      <polygon points="30,103 230,112 230,115 30,104" fill="#e31e2a"/>
      <polygon points="400,245 600,253 600,256 400,246" fill="#e31e2a"/>
    </svg>
    <div class="brand">
      <span class="brand__dot"></span>
      <span class="brand__name">O VITAL SYSTEMIQUE</span>
    </div>
  </section>

  <section class="card card--front" aria-label="Recto de la carte">
    <div class="brand">
      <span class="brand__dot"></span>
      <span class="brand__name">O VITAL SYSTEMIQUE</span>
    </div>

    <div class="person">
      <p class="person__name">Odile Ferrand</p>
      <p class="person__role">Chef de Projet</p>
      <ul class="contact-list">
        <li><span>318 Rue des Tilleuls Verts</span><svg class="icon" viewBox="0 0 12 12" aria-hidden="true"><path d="M6 0.5a3.6 3.6 0 0 0-3.6 3.6C2.4 7 6 11.5 6 11.5S9.6 7 9.6 4.1A3.6 3.6 0 0 0 6 0.5zm0 5a1.4 1.4 0 1 1 0-2.8 1.4 1.4 0 0 1 0 2.8z" fill="#3d3d3f"/></svg></li>
        <li><span>47150 VALMERANGE</span><span class="icon"></span></li>
        <li><span>+33 (0) 487 204 615</span><svg class="icon" viewBox="0 0 12 12" aria-hidden="true"><path d="M2.5 0.8l2 2.2-1 1.4c.7 1.5 1.8 2.6 3.3 3.3l1.4-1 2.2 2-1.1 1.9C5.5 10.2 1.8 6.5 0.6 2z" fill="#3d3d3f"/></svg></li>
        <li><span>06 42 93 17 58</span><svg class="icon" viewBox="0 0 12 12" aria-hidden="true"><rect x="3" y="0.5" width="6" height="11" rx="1" fill="#3d3d3f"/><rect x="4" y="1.8" width="4" height="7" fill="#fff"/></svg></li>
      </ul>
    </div>

    <div class="divider"></div>
    <div class="band"></div>

    <ul class="online">
      <li><span>o.ferrand@o-vitalsystemique.example</span><svg class="icon" viewBox="0 0 12 12" aria-hidden="true"><rect x="0.5" y="2" width="11" height="8" rx="1" fill="#3d3d3f"/><path d="M1 2.6l5 4 5-4" stroke="#fff" fill="none" stroke-width="1"/></svg></li>
      <li><span>www.cliniqorvane.example</span><svg class="icon" viewBox="0 0 12 12" aria-hidden="true"><circle cx="6" cy="6" r="5.5" fill="#3d3d3f"/><path d="M0.5 6h11M6 0.5c-2.4 3-2.4 8 0 11M6 0.5c2.4 3 2.4 8 0 11" stroke="#e31e2a" stroke-width="0.8" fill="none"/></svg></li>
    </ul>
  </section>

</main>
</body>
</html>
```